Cosmetics range packaging

Needing cosmetics logo design with our logo attached and showing you some examples of products we need logo and packaging (cosmetic box) designs.
Products e.g. palette is black so the printing would be a red metallic foil on the lid of the palette as a preference / guide. With the logo it would need to get a white letter M and a red metallic foil star. This is needed for the palette lid and also for the cardboard box packaging.

Some examples of the palette packaging and shape are attached below (competitor brands) just to show you what the shape is.

Target Market(s)

Women 15-60 years of age

Industry/Entity Type

Cosmetics

Requirements
Must have
• Our logo on it and packaging background is black.
Nice to have
• The logo preferably white letter M and red foil metallic star.
Should not have
• Open to ideas

```html
<!DOCTYPE html>
<html lang="en">
<head>
<meta charset="utf-8">
<title>Mirelle – 35 Color Pro Palette packaging</title>
<link rel="stylesheet" href="https://fonts.googleapis.com/css2?family=Dancing+Script:wght@500&display=swap">
<style>
  :root {
    --page: #ffffff;
    --foil-red: #b8281f;
    --lid-black: #121212;
    --ink: #1a1a1a;
    --brand-white: #ffffff;
    --fold-line: #9a9a9a;
  }
  html, body {
    margin: 0;
    padding: 0;
    width: 1200px;
    height: 754px;
    overflow: hidden;
    background: var(--page);
  }
  .artboard {
    display: block;
    width: 1200px;
    height: 754px;
  }
  .fill-red { fill: var(--foil-red); }
  .fill-black { fill: var(--lid-black); }
  .lid-edge { fill: none; stroke: var(--lid-black); stroke-width: 1.5; }
  .fold-line { fill: none; stroke: var(--fold-line); stroke-width: 1.2; }
  .product-title {
    font-family: "Dancing Script", cursive;
    font-weight: 500;
    font-size: 54px;
    fill: var(--ink);
  }
  .brand-name {
    font-family: "Dancing Script", cursive;
    font-weight: 500;
    font-size: 46px;
    fill: var(--brand-white);
  }
  .brand-name--side {
    font-size: 13px;
  }
</style>
</head>
<body>
<svg class="artboard" viewBox="0 0 1384 870" xmlns="http://www.w3.org/2000/svg" role="img" aria-label="Mirelle 35 Color Pro Palette lid design and box net">
  <defs>
    <symbol id="lid-art" viewBox="0 0 659 485">
      <rect class="fill-black" x="0" y="0" width="659" height="485"/>
      <polygon class="fill-red" points="0,8 222,107 439,0 492,0 444,279 659,485 0,485"/>
      <text class="brand-name" x="505" y="170" text-anchor="middle">Mirelle</text>
      <text class="product-title" x="31" y="444" textLength="482" lengthAdjust="spacingAndGlyphs">35 Color Pro Palette</text>
    </symbol>
  </defs>

  <!-- Palette lid -->
  <g class="palette-lid">
    <use href="#lid-art" x="91" y="66" width="659" height="485"/>
    <rect class="lid-edge" x="91" y="66" width="659" height="485"/>
  </g>

  <!-- Box net -->
  <g class="box-net">
    <rect class="fill-black" x="896" y="450" width="391" height="58"/>
    <rect class="fill-red" x="840" y="508" width="56" height="288"/>
    <rect class="fill-black" x="1287" y="508" width="55" height="288"/>
    <rect class="fill-red" x="896" y="796" width="391" height="60"/>
    <use href="#lid-art" x="896" y="508" width="391" height="288"/>
    <rect class="fold-line" x="896" y="508" width="391" height="288"/>
    <text class="brand-name brand-name--side" x="1314.5" y="767" text-anchor="middle">Mirelle</text>
  </g>
</svg>
</body>
</html>
```